Start up in business consultancy needs a business card

We need the business card's layout (we have already the logo). Our business is concerned on consultancy services delivered to companies on the matter of sustainability. Business card should be enough essentials and professional style.

Side A with the following info:
logo + a space for the claim (still to identify) + website of the company

Side B with the following info:
Name of business card holder + title of the business card holder + address of the company + space for mobile number, phone number, fax number + e-mail of business card holder + graphic details around.

Target Market(s)

Business of any sector

Industry/Entity Type

Business Service

Contact Information for Business Card

Name of the company:
Pianoverde srl
Società Benefit

Address of the company:
Via Lucerna, 7
21047 - Saronno (VA)

Website:
www.pianoverde.it

Name of the BC' holder:
Luca Ferentino

Title:
Co-fondatore

Email:
luca@pianoverde.it

Mobile:
+39 348 915 2074
Phone:
+39 348 915 2074
Fax:
+39 348 915 2074

Font styles to use
Other font styles liked:
• new gothic

```html
<!DOCTYPE html>
<html lang="it">
<head>
<meta charset="utf-8">
<title>Pianoverde – biglietto da visita</title>
<link href="https://fonts.googleapis.com/css2?family=Didact+Gothic&family=Open+Sans:ital,wght@1,800&display=swap" rel="stylesheet">
<style>
  :root {
    --page: #2b2b2d;
    --card: #1a1a1b;
    --card-edge: #101011;
    --brand-blue: #0a6fb8;
    --band-grey: #4a4d52;
    --text-light: #f1f1f1;
    --emboss: #3a3a3c;
  }
  * { margin: 0; padding: 0; box-sizing: border-box; }
  html, body { width: 799px; height: 1200px; overflow: hidden; }
  body {
    background: var(--page);
    font-family: "Didact Gothic", "Century Gothic", sans-serif;
    display: flex;
    flex-direction: column;
    align-items: center;
    justify-content: space-evenly;
  }
  .card {
    position: relative;
    width: 640px;
    height: 380px;
    background: var(--card);
    border: 1px solid var(--card-edge);
    box-shadow: 0 10px 30px rgba(0,0,0,.45);
    overflow: hidden;
  }

  /* Front */
  .front-mark {
    position: absolute;
    inset: 0;
    display: flex;
    align-items: center;
    justify-content: center;
    gap: 22px;
  }
  .front-mark .ring {
    width: 96px; height: 96px;
    border: 6px solid var(--emboss);
    border-radius: 50%;
  }
  .front-mark .wordmark {
    font-size: 54px;
    color: var(--emboss);
    letter-spacing: 1px;
  }

  /* Back */
  .bands { position: absolute; left: 0; top: 0; }

  .holder { position: absolute; left: 42px; top: 44px; }
  .holder-name {
    font-family: "Open Sans", sans-serif;
    font-style: italic;
    font-weight: 800;
    font-size: 26px;
    line-height: 32px;
    color: var(--brand-blue);
  }
  .holder-title { font-size: 14px; line-height: 18px; color: var(--text-light); margin-top: 2px; }

  .brand {
    position: absolute; left: 318px; top: 104px;
    display: flex; align-items: center; gap: 12px;
  }
  .brand .ring {
    width: 58px; height: 58px;
    border: 4px solid var(--brand-blue);
    border-radius: 50%;
  }
  .brand .wordmark { font-size: 36px; line-height: 44px; color: var(--brand-blue); }

  .company {
    position: absolute; left: 318px; top: 176px;
    font-size: 18px; line-height: 22px; color: var(--brand-blue);
  }
  .contacts {
    position: absolute; left: 318px; top: 204px;
    list-style: none;
    font-size: 15px; color: var(--text-light);
    line-height: 19px;
  }
  .contacts li { display: flex; align-items: center; gap: 10px; }
  .contacts svg { width: 13px; height: 13px; fill: var(--brand-blue); flex: none; }

  .address {
    position: absolute; left: 42px; top: 228px;
    font-size: 16px; line-height: 21px; color: var(--text-light);
  }

  .website {
    position: absolute; left: 262px; top: 334px;
    font-size: 17px; line-height: 22px; color: var(--text-light);
  }
</style>
</head>
<body>

  <section class="card card-front" aria-label="Fronte">
    <div class="front-mark">
      <span class="ring"></span>
      <span class="wordmark">pianoverde</span>
    </div>
  </section>

  <section class="card card-back" aria-label="Retro">
    <svg class="bands" width="640" height="380" viewBox="0 0 640 380" aria-hidden="true">
      <polygon points="0,296 262,296 249,316 0,316" fill="var(--band-grey)"/>
      <polygon points="249,316 272,304 640,304 640,380 200,380" fill="var(--brand-blue)"/>
    </svg>

    <div class="holder">
      <p class="holder-name">Luca Ferentino</p>
      <p class="holder-title">Co-fondatore</p>
    </div>

    <div class="brand">
      <span class="ring"></span>
      <span class="wordmark">pianoverde</span>
    </div>

    <p class="company">Pianoverde srl Società Benefit</p>

    <ul class="contacts">
      <li><svg viewBox="0 0 16 16"><rect x="4" y="0" width="8" height="16" rx="2"/></svg>+39 348 915 2074</li>
      <li><svg viewBox="0 0 16 16"><path d="M1 6 Q8 0 15 6 L12 8 L10 5 H6 L4 8 Z M3 9 H13 V15 H3 Z"/></svg>+39 348 915 2074</li>
      <li><svg viewBox="0 0 16 16"><rect x="4" y="1" width="8" height="5"/><rect x="1" y="6" width="14" height="6"/><rect x="4" y="11" width="8" height="4"/></svg>+39 348 915 2074</li>
      <li><svg viewBox="0 0 16 16"><path d="M0 3 H16 V13 H0 Z M0 3 L8 9 L16 3" stroke="var(--card)" stroke-width="1"/></svg>luca@pianoverde.it</li>
    </ul>

    <p class="address">Via Lucerna, 7<br>21047 - Saronno (VA)</p>

    <p class="website">www.pianoverde.it</p>
  </section>

</body>
</html>
```